Product labels for new supplements business targeting high performing creative people

I need a label design for different supplements like Whey, BCAA, Melatonin etc. that I could customize for each use case separately.

The brand is called wovenpath.life, and it would be the first design of the labels. We haven't sold any products yet, but the target audience is people with growth mindset, people who want to be as efficient as possible and are constantly looking to improve their lifestyle. As part of that, they are also working out, but don't know much about supplements yet. Mostly people between 20-34.

I don't have a too specific idea of the expected design, though it should be light, warm, smart and minimalist, maybe have some patterns. It should looks smart and clean (and expensive). Orange and golden might be the additional colors for white. I have attached the templates of some products that I plan to sell and also the logo of the brand.

Here's what I have used for inspiration:
Brands that I like and are somewhat similar in concept: https://www.plarnix.com/ (!!specially the way they
bring "how the product helps them" in focus, not "what the product is" & https://www.bevo.care/ &
https://www.moflesta.com/sport/ & https://en.calwostor.fr/ &
https://artboardhub.com/profiles/mirelfondastudio/designs/461827

Here's how different products look like: https://bondrexa.com/catalog

Target Market(s)

target audience is people with growth mindset, people who want to be as efficient as possible and are constantly looking to improve their lifestyle. As part of that, they are also working out, but don't know much about supplements yet. Mostly people between 20-34.

Industry/Entity Type

Supplements

Font styles to use
Sans Serif

Colors
FFC000
F8CF3A
FAE287
FDF2CF
FEFAEE
F0912C
F2A743
F7CA91
FBE8D2
FDF5EE
EE7325
F08F49
F5BC92
FAE3D3
FDF4ED

Requirements
Must have
• Clean, smart and minimalist design that can be applied for different products in different sizes, like Whey protein, BCAA, vitamins etc. available here: https://bondrexa.com/catalog
Nice to have
• Patterns, expensive look
Should not have
• Doodles, too many colors

```html
<!DOCTYPE html>
<html lang="en">
<head>
<meta charset="UTF-8">
<title>wovenpath.life — Melatonin label</title>
<link rel="stylesheet" href="https://fonts.googleapis.com/css2?family=Bebas+Neue&family=Poppins:wght@400;500;600&display=swap">
<style>
  :root {
    --backdrop: #efefef;
    --label: #ffffff;
    --ink: #111111;
    --gold: #c9a24a;
    --gold-light: #f3dfa6;
    --gold-pale: #fdf2cf;
  }
  * { margin: 0; padding: 0; box-sizing: border-box; }
  html, body { width: 1200px; height: 1200px; overflow: hidden; }
  body {
    background: var(--backdrop);
    font-family: "Poppins", sans-serif;
    color: var(--ink);
    position: relative;
  }
  .label {
    position: absolute;
    left: 223px;
    top: 35px;
    width: 754px;
    height: 1130px;
    background: var(--label);
    box-shadow: 0 2px 18px rgba(0,0,0,0.06);
  }
  .label > * { position: absolute; left: 0; width: 100%; text-align: center; }
  .brand-dot {
    top: 118px;
    left: 50%;
    width: 58px;
    height: 58px;
    margin-left: -29px;
    border-radius: 50%;
    background: var(--gold);
  }
  .brand-name {
    top: 238px;
    font-size: 76px;
    font-weight: 500;
    letter-spacing: 0.5px;
    line-height: 1;
  }
  .sleep-mark {
    top: 500px;
    left: 490px;
    width: 130px;
    text-align: left;
    font-size: 46px;
    font-weight: 600;
    color: var(--gold);
    line-height: 1;
  }
  .sleep-mark span:nth-child(2) { position: relative; top: -10px; }
  .sleep-mark span:nth-child(3) { position: relative; top: -20px; }
  .product-name {
    top: 614px;
    font-family: "Bebas Neue", sans-serif;
    font-size: 138px;
    letter-spacing: 7px;
    line-height: 1;
    padding-left: 7px;
  }
  .dose {
    top: 778px;
    font-size: 34px;
    font-weight: 600;
    letter-spacing: 3px;
    line-height: 1;
  }
  .benefits {
    top: 856px;
    font-size: 27px;
    font-weight: 400;
    letter-spacing: 2px;
    line-height: 44px;
  }
  .product-info {
    top: 1044px;
    font-size: 25px;
    font-weight: 400;
    letter-spacing: 1.5px;
    line-height: 1;
  }
  .gold-band {
    top: 1084px;
    height: 12px;
    background: linear-gradient(90deg, var(--gold-light), var(--gold-pale) 50%, var(--gold-light));
  }
</style>
</head>
<body>
  <main class="label">
    <div class="brand-dot"></div>
    <div class="brand-name">wovenpath.life</div>
    <div class="sleep-mark" aria-hidden="true"><span>z</span><span>z</span><span>z</span></div>
    <h1 class="product-name">Melatonin</h1>
    <div class="dose">- 1MG -</div>
    <p class="benefits">FALL ASLEEP FASTER*<br>STAY ASLEEP LONGER*</p>
    <div class="product-info">DIETARY SUPPLEMENT | 60 TABLETS</div>
    <div class="gold-band"></div>
  </main>
</body>
</html>
```